Explainer Video Landing Page

We will soon have an "explainer" video which will explain to people in a graphical way what it is we do and the solutions we provide. Our current landing page design, located at http://www.lanternvoicecentral.com has a lot of different elements that we like, but won't focus on the new video we have as the "hero". We will want this new landing page to really showcase the video. Some of the other design elements we need are :
1- A link to "Get a Quote Online", in some way. This is the "goal" of the landing page.
2- We'll want some content sections under the video
3- We'll want the lead gen form to be there as well.
As an example, have a look at what BrisklyFern did. http://www.brisklyfern.com/
We like their example, but find it a bit busy. Our design should be cleaner with more whitespace. They are doing a lot of good things on that page that we'll want to mimic, like adding testimonials and existing customer logos.
Thank you in advance for participating in our design project.
Target Market(s)
Small and Mid-size Businesses. This will be a B2B landing page, focused on the communications needs of business.
Look and feel
Each slider illustrates characteristics of the customer's brand and the style your logo design should communicate.

```html
<!DOCTYPE html>
<html lang="en">
<head>
<meta charset="utf-8">
<title>Corvalis – The Corvalis Vibe</title>
<link href="https://fonts.googleapis.com/css2?family=Ubuntu:wght@300;400;500;700&display=swap" rel="stylesheet">
<style>
:root{
  --cyan:#35d8f0;
  --hero:#2cc6ea;
  --hero-light:#3ad6f1;
  --ink:#2b2b2b;
  --heading:#454545;
  --dark:#4a4646;
  --white:#ffffff;
  --bezel:#1c1c1c;
  --silver:#c9cacc;
}
*{margin:0;padding:0;box-sizing:border-box}
html,body{width:1200px;height:1182px;overflow:hidden;background:var(--white);font-family:'Ubuntu',sans-serif}
.page{position:relative;width:1200px;height:1182px;overflow:hidden}

.topbar{position:absolute;left:0;top:0;width:1200px;height:53px;background:var(--cyan);color:var(--white);font-size:13px;font-weight:500}
.contact{position:absolute;top:17px;display:flex;align-items:center;gap:9px}
.contact svg{width:20px;height:20px}
.contact--phone{left:144px}
.contact--mail{left:290px}
.contact--chat{left:480px}
.account{position:absolute;left:842px;top:20px;font-size:12.5px;font-weight:700;letter-spacing:.5px;display:flex;gap:18px}
.search{position:absolute;left:1018px;top:0;width:182px;height:53px;background:var(--dark)}
.search svg{position:absolute;left:80px;top:14px;width:24px;height:24px}

.header{position:absolute;left:0;top:53px;width:1200px;height:159px;background:var(--white)}
.brand{position:absolute;left:146px;top:60px;display:flex;align-items:center;gap:10px}
.brand__mark{width:22px;height:22px;border-radius:50%;background:var(--ink)}
.brand__name{font-size:26px;font-weight:500;color:var(--ink)}
.nav{position:absolute;left:455px;top:83px;display:flex;align-items:center;font-size:15.5px;font-weight:700;color:var(--ink)}
.nav a{color:inherit;text-decoration:none}
.nav a.is-active{color:var(--cyan)}
.nav .sep{margin:0 13px;font-size:12px}

.hero{position:absolute;left:0;top:212px;width:1200px;height:678px;background:linear-gradient(135deg,var(--hero) 0%,var(--hero-light) 50%,var(--hero) 100%);color:var(--white);text-align:center}
.hero__title{position:absolute;top:50px;width:100%;font-size:37px;font-weight:700;letter-spacing:3.5px}
.hero__lead{position:absolute;top:104px;width:100%;font-size:21.5px;font-weight:300;line-height:26px}

.laptop{position:absolute;left:256px;top:410px;width:690px;height:464px;background:var(--bezel);border-radius:16px 16px 0 0}
.laptop__screen{position:absolute;left:20px;top:28px;width:650px;height:410px;background:linear-gradient(100deg,#a9a78c 0%,#ccc7a4 45%,#8e8270 75%,#5f5a55 100%)}
.play{position:absolute;left:292px;top:183px;width:64px;height:64px;border-radius:50%;background:rgba(255,255,255,.92)}
.play svg{position:absolute;left:23px;top:19px;width:22px;height:26px}
.laptop__base{position:absolute;left:175px;top:874px;width:850px;height:26px;background:linear-gradient(180deg,#e8e9ea 0%,var(--silver) 55%,#7e7f82 100%);border-radius:0 0 60px 60px / 0 0 20px 20px}
.laptop__notch{position:absolute;left:366px;top:0;width:118px;height:9px;background:#b3b4b6;border-radius:0 0 8px 8px}

.features__title{position:absolute;top:972px;width:100%;text-align:center;font-size:33px;font-weight:700;letter-spacing:4px;color:var(--heading)}
.feature-icon{position:absolute;top:1060px;width:98px;height:98px;border-radius:50%;background:var(--cyan)}
.feature-icon svg{position:absolute;left:19px;top:19px;width:60px;height:60px}
</style>
</head>
<body>
<div class="page">
  <div class="topbar">
    <div class="contact contact--phone">
      <svg viewBox="0 0 20 20"><circle cx="10" cy="10" r="10" fill="#fff"/><path d="M6 5.5l2 -.5 1.2 2.6-1.3 1c.6 1.3 1.5 2.2 2.8 2.8l1-1.3 2.6 1.2-.5 2c-4 .2-8-3.8-7.8-7.8z" fill="#35d8f0"/></svg>
      <span>(555) 555 555</span>
    </div>
    <div class="contact contact--mail">
      <svg viewBox="0 0 20 20"><circle cx="10" cy="10" r="10" fill="#fff"/><rect x="5" y="6.5" width="10" height="7" rx="1" fill="#35d8f0"/><path d="M5.5 7l4.5 3.5L14.5 7" stroke="#fff" stroke-width="1.2" fill="none"/></svg>
      <span>sales@corvalis.com.</span>
    </div>
    <div class="contact contact--chat">
      <svg viewBox="0 0 20 20"><circle cx="10" cy="10" r="10" fill="#fff"/><circle cx="10" cy="9.5" r="4.5" fill="#35d8f0"/><path d="M7 13l-1 2.5 3-1.5z" fill="#35d8f0"/></svg>
      <span>live chat</span>
    </div>
    <div class="account"><span>SIGN IN</span><span>I</span><span>SIGN UP</span></div>
    <div class="search">
      <svg viewBox="0 0 24 24"><circle cx="14" cy="10" r="6" stroke="#fff" stroke-width="2.6" fill="none"/><path d="M9.5 14.5L4 20" stroke="#fff" stroke-width="3" stroke-linecap="round"/></svg>
    </div>
  </div>

  <header class="header">
    <div class="brand">
      <span class="brand__mark"></span>
      <span class="brand__name">Corvalis</span>
    </div>
    <nav class="nav">
      <a class="is-active" href="#">HOME</a><span class="sep">I</span>
      <a href="#">PRICING &amp; PLAN</a><span class="sep">I</span>
      <a href="#">FEATURES</a><span class="sep">I</span>
      <a href="#">PHONES</a><span class="sep">I</span>
      <a href="#">LEARN MORE</a><span class="sep">I</span>
      <a href="#">BLOG</a>
    </nav>
  </header>

  <section class="hero">
    <h1 class="hero__title">THE CORVALIS VIBE</h1>
    <p class="hero__lead">Check out Corvalis's Corporate Culture video to get a sense of the kind of people<br>you'll be working with at Corvalis</p>
  </section>

  <div class="laptop">
    <div class="laptop__screen" role="img" aria-label="Corporate culture video still: young businessman in a suit in front of a city skyline">
      <div class="play"><svg viewBox="0 0 22 26"><path d="M2 1l19 12L2 25z" fill="#7a7a7a"/></svg></div>
    </div>
  </div>
  <div class="laptop__base"><div class="laptop__notch"></div></div>

  <h2 class="features__title">FEATURES</h2>
  <div class="feature-icon" style="left:210px">
    <svg viewBox="0 0 60 60"><rect x="2" y="14" width="56" height="34" rx="3" fill="#fff"/><path d="M4 16l26 18 26-18" stroke="#35d8f0" stroke-width="4" fill="none"/></svg>
  </div>
  <div class="feature-icon" style="left:437px">
    <svg viewBox="0 0 60 60"><rect x="16" y="2" width="28" height="56" rx="5" fill="#fff"/><rect x="20" y="8" width="20" height="20" fill="#35d8f0"/><g fill="#35d8f0"><rect x="20" y="33" width="5" height="4"/><rect x="27.5" y="33" width="5" height="4"/><rect x="35" y="33" width="5" height="4"/><rect x="20" y="40" width="5" height="4"/><rect x="27.5" y="40" width="5" height="4"/><rect x="35" y="40" width="5" height="4"/></g></svg>
  </div>
  <div class="feature-icon" style="left:664px">
    <svg viewBox="0 0 60 60"><path d="M8 32a22 22 0 0 1 44 0" stroke="#fff" stroke-width="4" fill="none"/><rect x="3" y="28" width="11" height="16" rx="5" fill="#fff"/><rect x="46" y="28" width="11" height="16" rx="5" fill="#fff"/><path d="M51 44c0 8-8 12-18 12" stroke="#fff" stroke-width="3" fill="none"/></svg>
  </div>
  <div class="feature-icon" style="left:891px">
    <svg viewBox="0 0 60 60"><path d="M14 6l10 2 4 12-6 5c3 6 8 11 14 14l5-6 12 4 2 10c-22 4-45-19-41-41z" fill="#fff"/></svg>
  </div>
</div>
</body>
</html>
```